Business Card - Professional Minimalist - Double sided

We appreciate minimalist logo/web/collateral designs that allow design to tell a story. We want to relay a professional image/approach but throwing in a splash of modern when we’re able so long as it’s not distracting. Think 75% classic corporate, 25% modern. Open to black or white design, not sure which might look the best.

Target Market(s)

Senior executives or related government affairs contacts within the agriculture, energy, and defense industries (i.e., potential clients) but located outside of Washington, DC. Most potential clients based in DC with be familiar with both of us and our shared history.

Industry/Entity Type

Consulting

Contact Information for Business Card

Name: Daniel R. Whitlock
Title: Co-Founder & Partner
Address: 418 Bramblewood Ave. SE | Suite 2716 | Washington, D.C. 20019
Phone: (202) 555-0187
Email: Daniel@HollerbyWhitlock.com

Font styles to use
Serif

Colors

Designer to choose only greyscale colors for use in the design.

Requirements
Must have
• Name: Daniel R. Whitlock
Phone: (202) 555-0187

```html
<!DOCTYPE html>
<html lang="en">
<head>
<meta charset="utf-8">
<title>Hollerby Whitlock Group – Business Card</title>
<link href="https://fonts.googleapis.com/css2?family=Lato:wght@400;700;900&display=swap" rel="stylesheet">
<style>
  :root {
    --stage: #3b3c3f;
    --ink: #0a0a0a;
    --paper: #ffffff;
    --grey-dark: #444546;
    --grey-mid: #6d6e70;
    --grey-band: #a7a8aa;
  }
  * { box-sizing: border-box; margin: 0; padding: 0; }
  html, body { width: 1200px; height: 900px; overflow: hidden; }
  body {
    background: var(--stage);
    font-family: "Lato", Arial, sans-serif;
    position: relative;
  }
  .card {
    position: absolute;
    width: 560px;
    height: 320px;
    border-radius: 22px;
    overflow: hidden;
  }
  .card--back { left: 80px; top: 90px; }
  .card--front { left: 560px; top: 480px; background: var(--paper); }

  .back-field {
    position: absolute; inset: 0;
    background: linear-gradient(135deg, #111 0%, var(--ink) 60%, #161616 100%);
  }
  .back-name {
    position: absolute;
    left: 330px; top: 176px;
    display: flex; align-items: center; gap: 8px;
    color: var(--paper);
    font-size: 15px; font-weight: 700; letter-spacing: 1.5px;
  }
  .back-name .mark-square { width: 12px; height: 12px; background: var(--paper); }

  .front-art { position: absolute; inset: 0; }

  .identity {
    position: absolute; right: 40px; top: 34px; text-align: right;
  }
  .identity__name {
    font-size: 30px; font-weight: 900; color: var(--grey-dark); letter-spacing: -0.3px;
  }
  .identity__title {
    font-size: 16px; color: var(--grey-mid); margin-top: 2px;
  }

  .brand {
    position: absolute; left: 44px; top: 150px;
    display: flex; align-items: center; gap: 10px;
    color: var(--grey-dark);
  }
  .brand .mark-square { width: 24px; height: 24px; border: 3px solid var(--grey-dark); flex: none; }
  .brand__name {
    font-size: 15px; font-weight: 700; letter-spacing: 2px; line-height: 19px;
    text-transform: uppercase;
  }

  .contact {
    position: absolute; right: 24px; top: 176px;
    color: var(--paper); font-size: 12.5px; line-height: 17px; text-align: right;
  }
  .contact__row { display: flex; justify-content: flex-end; align-items: center; gap: 8px; }
  .contact__icon { width: 12px; height: 12px; flex: none; }
  .contact__spacer { width: 12px; flex: none; }
</style>
</head>
<body>

<section class="card card--back">
  <div class="back-field" role="img" aria-label="Repeating monogram pattern in dark grey on black"></div>
  <div class="back-name"><span class="mark-square"></span>HOLLERBY WHITLOCK</div>
</section>

<section class="card card--front">
  <svg class="front-art" viewBox="0 0 560 320" width="560" height="320" aria-hidden="true">
    <path d="M0,242 C120,235 230,238 310,190 C390,140 440,100 560,92 L560,320 L0,320 Z" fill="var(--grey-band)"/>
    <path d="M0,256 C120,249 230,252 310,204 C390,154 440,114 560,106 L560,320 L0,320 Z" fill="var(--paper)"/>
    <path d="M0,262 C120,255 230,258 310,210 C390,160 440,120 560,112 L560,320 L0,320 Z" fill="var(--ink)"/>
  </svg>

  <div class="identity">
    <div class="identity__name">Daniel R. Whitlock</div>
    <div class="identity__title">Co-Founder &amp; Partner</div>
  </div>

  <div class="brand">
    <span class="mark-square"></span>
    <span class="brand__name">Hollerby Whitlock<br>Group</span>
  </div>

  <div class="contact">
    <div class="contact__row"><span>418 Bramblewood Ave. SE</span><span class="contact__spacer"></span></div>
    <div class="contact__row"><span>Suite 2716</span><span class="contact__spacer"></span></div>
    <div class="contact__row"><span>Washington, D.C. 20019</span><span class="contact__spacer"></span></div>
    <div class="contact__row"><span>(202) 555-0187</span>
      <svg class="contact__icon" viewBox="0 0 12 12"><path d="M2.5 1 L4.5 1 L5 3.5 L3.8 4.4 C4.4 5.8 5.6 7.2 7.4 8 L8.4 6.8 L11 7.4 L11 9.4 C11 10.3 10.2 11 9.3 10.9 C5 10.5 1.5 7 1.1 2.7 C1 1.8 1.6 1 2.5 1 Z" fill="#fff"/></svg>
    </div>
    <div class="contact__row"><span>Daniel@HollerbyWhitlock.com</span>
      <svg class="contact__icon" viewBox="0 0 12 12"><rect x="0.5" y="2.5" width="11" height="7.5" fill="#fff"/><path d="M0.8 2.8 L6 7 L11.2 2.8" stroke="#0a0a0a" stroke-width="1" fill="none"/></svg>
    </div>
    <div class="contact__row"><span>www.HollerbyWhitlock.com</span>
      <svg class="contact__icon" viewBox="0 0 12 12"><circle cx="6" cy="6" r="5" fill="none" stroke="#fff" stroke-width="1.2"/><path d="M1 6 H11 M6 1 C3.5 3.5 3.5 8.5 6 11 M6 1 C8.5 3.5 8.5 8.5 6 11" stroke="#fff" stroke-width="0.9" fill="none"/></svg>
    </div>
  </div>
</section>

</body>
</html>
```